- Redesign our business card
- Logo remains unchanged
- Current business card attached

Target Market(s)

We are a property management company

Industry/Entity Type

Business

```html
<!DOCTYPE html>
<html lang="en">
<head>
<meta charset="utf-8">
<title>Harlow Property Group – Business Card</title>
<link rel="stylesheet" href="https://fonts.googleapis.com/css2?family=Arimo:wght@400;700&family=Roboto+Condensed:wght@300;400;700&display=swap">
<style>
  :root {
    --stage: #161616;
    --card-front: #efeff0;
    --card-back: #6d6e71;
    --brand-olive: #7d7a45;
    --brand-grey: #6d6e71;
    --accent-sand: #ddd2a4;
    --text-light: #ffffff;
    --text-muted: #dcdcdd;
    --rule: #9a9b9e;
  }
  * { margin: 0; padding: 0; box-sizing: border-box; }
  html, body {
    width: 1200px; height: 900px; overflow: hidden;
    background: var(--stage);
  }
  .canvas { position: relative; width: 1200px; height: 900px; }

  .card {
    position: absolute;
    left: 262px; width: 677px; height: 382px;
    border-radius: 12px;
  }
  .card--front { top: 47px; background: var(--card-front); }
  .card--back { top: 471px; background: var(--card-back); color: var(--text-light);
    font-family: "Roboto Condensed", "Arial Narrow", sans-serif; }

  /* Front */
  .brand-square {
    position: absolute; left: 66px; top: 74px;
    width: 170px; height: 170px;
    background: var(--brand-olive);
  }
  .brand-name {
    position: absolute; left: 64px; top: 268px;
    font-family: "Arimo", Arial, sans-serif;
    font-weight: 700; font-size: 33px; letter-spacing: 0.5px;
    color: var(--brand-grey); white-space: nowrap;
  }
  .brand-tagline {
    position: absolute; left: 66px; top: 307px;
    font-family: "Arimo", Arial, sans-serif;
    font-weight: 400; font-size: 26px; letter-spacing: 0.6px;
    color: var(--brand-grey); white-space: nowrap;
  }

  /* Back */
  .person { position: absolute; left: 297px; top: 33px; }
  .person__name { font-weight: 700; font-size: 23px; letter-spacing: 0.4px; }
  .person__title { font-weight: 300; font-size: 17px; color: var(--text-muted); margin-top: 2px; }

  .services {
    position: absolute; right: 429px; top: 197px;
    text-align: right; list-style: none;
    color: var(--accent-sand); font-size: 17px; line-height: 27px; font-weight: 400;
  }
  .divider-v {
    position: absolute; left: 270px; top: 159px;
    width: 1px; height: 143px; background: var(--rule);
  }
  .contact {
    position: absolute; left: 297px; top: 170px;
    list-style: none; font-size: 17px; line-height: 26.5px; font-weight: 300;
  }
  .divider-h {
    position: absolute; left: 38px; right: 38px; top: 317px;
    height: 1px; background: var(--rule);
  }
  .web {
    position: absolute; left: 0; right: 0; top: 333px;
    text-align: center; font-size: 17px; font-weight: 300;
  }
</style>
</head>
<body>
<main class="canvas">
  <section class="card card--front" aria-label="Business card front">
    <div class="brand-square"></div>
    <p class="brand-name">HARLOW PROPERTY GROUP</p>
    <p class="brand-tagline">STRATA MANAGEMENT SERVICES</p>
  </section>

  <section class="card card--back" aria-label="Business card back">
    <div class="person">
      <p class="person__name">DANIEL HARLOW</p>
      <p class="person__title">Licensed Strata Manager</p>
    </div>
    <ul class="services">
      <li>Strata Management</li>
      <li>Community Management</li>
      <li>Property Management</li>
    </ul>
    <div class="divider-v"></div>
    <ul class="contact">
      <li>PO BOX 48, Marlowe Heights NSW 2031</li>
      <li>12/6-20 Fenwick Street Ashgrove NSW 2045</li>
      <li>T: 02 5550 0143</li>
      <li>F: 02 5550 0198</li>
      <li>M: 0400 555 217</li>
    </ul>
    <div class="divider-h"></div>
    <p class="web">info@harlowproperty.com.au &nbsp;-&nbsp; www.harlowproperty.com.au</p>
  </section>
</main>
</body>
</html>
```